Letterhead for Dorian Welk

I need a letterhead based on the business card design

Industry/Entity Type

Business

Requirements
Must have
• Footer: Dorian Welk Naturopath
Shop 4123c, 46 Carrow Lane, Sydney 2000

```html
<!DOCTYPE html>
<html lang="en">
<head>
<meta charset="utf-8">
<title>Dorian Welk Naturopath – Letterhead</title>
<link rel="stylesheet" href="https://fonts.googleapis.com/css2?family=Raleway:wght@300;400&family=Open+Sans:wght@400&display=swap">
<style>
  :root {
    --orange: #f39a1e;
    --orange-light: #f7b968;
    --orange-pale: #fbd7a6;
    --ink: #4a4a4a;
    --paper: #ffffff;
  }
  html, body {
    margin: 0;
    padding: 0;
    width: 900px;
    height: 1200px;
    overflow: hidden;
    background: var(--paper);
  }
  .letterhead {
    position: relative;
    width: 900px;
    height: 1200px;
    background: var(--paper);
    font-family: "Open Sans", Arial, sans-serif;
    color: var(--ink);
  }
  .side-band {
    position: absolute;
    left: 0;
    top: 0;
    width: 245px;
    height: 1200px;
    background: var(--orange);
  }
  .brand {
    position: absolute;
    left: 0;
    top: 122px;
    width: 245px;
    text-align: center;
    color: var(--paper);
    font-family: "Raleway", Arial, sans-serif;
    font-weight: 300;
  }
  .brand-name {
    font-size: 31px;
    letter-spacing: 2px;
    line-height: 1;
  }
  .brand-tagline {
    margin-top: 12px;
    font-size: 11px;
    letter-spacing: 4px;
  }
  .leaf-artwork {
    position: absolute;
    left: 0;
    top: 470px;
    width: 245px;
    height: 570px;
    background:
      radial-gradient(ellipse at 45% 45%, var(--orange-pale) 0%, var(--orange-light) 45%, var(--orange) 80%);
    opacity: 0.85;
  }
  .side-contact {
    position: absolute;
    left: 22px;
    top: 1118px;
    color: var(--paper);
    font-size: 9px;
    line-height: 1.5;
  }
  .letter {
    position: absolute;
    left: 300px;
    top: 170px;
    width: 530px;
    font-size: 11.5px;
    line-height: 1.65;
  }
  .letter-date {
    text-align: right;
    margin: 0 0 30px;
  }
  .letter p {
    margin: 0 0 16px;
  }
  .letter-signature {
    margin-top: 34px;
  }
  .footer {
    position: absolute;
    left: 285px;
    right: 70px;
    top: 1140px;
    color: var(--orange);
    font-size: 9.5px;
    line-height: 1.5;
  }
  .footer-address {
    position: absolute;
    left: 0;
    top: 8px;
  }
  .footer-contact {
    position: absolute;
    right: 0;
    top: 0;
    text-align: right;
  }
</style>
</head>
<body>
  <div class="letterhead">
    <aside class="side-band">
      <div class="brand">
        <div class="brand-name">DORIAN WELK</div>
        <div class="brand-tagline">NATUROPATHY</div>
      </div>
      <div class="leaf-artwork" role="img" aria-label="Large translucent leaf illustration in pale orange tones"></div>
      <div class="side-contact">
        www.dorianwelk.com<br>
        hello@dorianwelk.com
      </div>
    </aside>

    <main class="letter">
      <p class="letter-date">8 May 2014</p>
      <p>Dear Marcus</p>
      <p>Thank you for visiting the clinic last week and for taking the time to talk through your health goals with me. As discussed, I have prepared a gentle plan that supports your digestion, improves your sleep and helps you manage the stress of your working week. The plan combines simple dietary changes, a short course of herbal tonics and a few daily habits that are easy to keep. Please read through the enclosed notes at your own pace and write down any questions that come up. Most people notice a steady change within the first few weeks, although every body responds in its own time and we will adjust the plan as needed.</p>
      <p>Your next appointment is booked for the morning of the twentieth. At that visit we will review your food diary, check how you are sleeping and decide whether to continue with the current tonic or move to the second stage of the plan.</p>
      <p>If you feel unwell or notice any change that worries you, please call the clinic straight away so we can talk it over together.</p>
      <p>Again, thank you for placing your trust in my care. I look forward to seeing you soon and to hearing how the first few weeks have gone. Until then, rest well, drink plenty of water and take a short walk outdoors each day.</p>
      <p>Yours sincerely,</p>
      <p class="letter-signature">Dorian Welk</p>
    </main>

    <footer class="footer">
      <div class="footer-address">Dorian Welk Naturopath &nbsp;|&nbsp; Shop 4123c, 46 Carrow Lane, Sydney 2000</div>
      <div class="footer-contact">
        0412 555 731<br>
        hello@dorianwelk.com
      </div>
    </footer>
  </div>
</body>
</html>
```